Water Filtration Company needs a business card design using our existing logo/colours!

We design and manufacture and export specialised water filtration equipment. Our equipment will take unclean dirty water and filters to safe clean drinkable water.
We would like to see designs using our existing logo and colours (see attached "Palette") that represents clean safe drinking water (fresh, clean designs but still professional and modern). Our customers are other businesses who supply water filtration equipment, governments, and private individuals.
BUSINESS CARD DETAILS (Common details):
Tel: + 61 7 55 419 276
www: brindlepeak.com.au
Address: 3/47 Cordwell Parade
Marlow Flats NSW 2593 Australia
(please include the word Australia as we are an international company)
Must include: COMMERCIAL WATER FILTRATION EQUIPMENT
NAME NO 1:
Owen Pritch
General Manager
Mobile: +61 427 38 91 04
Email: owen@brindlepeak.com.au
NAME NO. 2:
Gina Rosk
Business Manager
Mobile: +61 409 572 148
Email: gina@brindlepeak.com.au
Must Have:
1) PRINT READY IN .AI & .PDF FORMATS
2) Also saved in file format .ai (Adobe Illustrator - compatible with CS4)
3) Use existing LOGO & COLOURS: Please use our logo (see attached file)
4) FONTS: we have used Avenir & Helvetica in the past but are open to other font types for the address etc.
Thank you!

```html
<!DOCTYPE html>
<html lang="en">
<head>
<meta charset="utf-8">
<title>Brindle Peak — Business Cards</title>
<link rel="stylesheet" href="https://fonts.googleapis.com/css2?family=Nunito+Sans:wght@400;600;700&display=swap">
<style>
  :root {
    --backdrop: #e6e8e9;
    --teal-light: #2da3b4;
    --teal-deep: #0a5a7d;
    --teal-ink: #17708c;
    --teal-accent: #2aa0b4;
    --card-white: #f2f3f3;
    --ink: #2b2e30;
    --ink-soft: #45494c;
    --white: #ffffff;
    --white-soft: rgba(255, 255, 255, 0.82);
  }
  * { margin: 0; padding: 0; box-sizing: border-box; }
  html, body { width: 1200px; height: 900px; overflow: hidden; }
  body {
    background: var(--backdrop);
    font-family: "Nunito Sans", "Helvetica Neue", Arial, sans-serif;
    position: relative;
  }
  .card {
    position: absolute;
    width: 560px;
    height: 320px;
    border-radius: 3px;
    box-shadow: 0 10px 26px rgba(0, 0, 0, 0.16);
    overflow: hidden;
  }

  /* Front */
  .card--front {
    left: 70px;
    top: 100px;
    background: linear-gradient(135deg, var(--teal-light) 0%, #1a82a0 50%, var(--teal-deep) 100%);
    color: var(--white);
  }
  .card--front .wordmark {
    position: absolute;
    right: 48px;
    top: 98px;
    font-size: 58px;
    font-weight: 700;
    letter-spacing: -0.5px;
    line-height: 1;
    color: var(--white);
  }
  .card--front .tagline {
    position: absolute;
    right: 48px;
    bottom: 70px;
    font-size: 15px;
    font-weight: 400;
    letter-spacing: 0.6px;
    color: var(--white-soft);
  }

  /* Back */
  .card--back {
    left: 570px;
    top: 470px;
    background: var(--card-white);
    color: var(--ink);
  }
  .card--back .watermark {
    position: absolute;
    right: 0;
    top: 0;
    width: 300px;
    height: 200px;
    background: radial-gradient(ellipse at 75% 25%, rgba(42, 160, 180, 0.10), rgba(42, 160, 180, 0) 70%);
  }
  .card--back .wordmark {
    position: absolute;
    left: 36px;
    top: 46px;
    font-size: 46px;
    font-weight: 700;
    letter-spacing: -0.5px;
    line-height: 1;
    color: var(--teal-ink);
  }
  .person {
    position: absolute;
    left: 36px;
    bottom: 48px;
  }
  .person__name {
    font-size: 22px;
    font-weight: 400;
    letter-spacing: 0.8px;
    text-transform: uppercase;
    color: var(--ink);
  }
  .person__role {
    font-size: 16px;
    color: var(--ink-soft);
    margin-top: 2px;
  }
  .divider {
    position: absolute;
    left: 290px;
    top: 136px;
    width: 1px;
    height: 150px;
    background: var(--teal-accent);
  }
  .contact {
    position: absolute;
    left: 306px;
    top: 136px;
    font-size: 13px;
    line-height: 19px;
    color: var(--ink);
  }
  .contact__row { display: flex; }
  .contact__label {
    width: 18px;
    color: var(--teal-accent);
    font-weight: 600;
  }
  .contact__indent { padding-left: 18px; }
  .contact__web { color: var(--teal-accent); }
</style>
</head>
<body>

  <section class="card card--front" aria-label="Business card front">
    <div class="wordmark">brindle peak</div>
    <div class="tagline">COMMERCIAL WATER FILTRATION EQUIPMENT</div>
  </section>

  <section class="card card--back" aria-label="Business card back">
    <div class="watermark" role="img" aria-label="Faint leaf line decoration"></div>
    <div class="wordmark">brindle peak</div>

    <div class="person">
      <div class="person__name">Owen Pritch</div>
      <div class="person__role">General Manager</div>
    </div>

    <div class="divider"></div>

    <div class="contact">
      <div class="contact__row"><span class="contact__label">M</span><span>+61 427 38 91 04</span></div>
      <div class="contact__row"><span class="contact__label">T</span><span>+61 7 55 419 276</span></div>
      <div class="contact__row"><span class="contact__label">E</span><span>owen@brindlepeak.com.au</span></div>
      <div class="contact__indent">3/47 Cordwell Parade</div>
      <div class="contact__indent">Marlow Flats NSW 2593 Australia</div>
      <div class="contact__indent contact__web">www.brindlepeak.com.au</div>
    </div>
  </section>

</body>
</html>
```